Birch Lane Associates is a Company that provides business solutions to local companies.

I need a flyer for Birch Lane Associates because I will be offering services to local businesses in Colorado. We offer a whole list of services that could help build your business or cut unnecessary costs. Please make it front and back. Include (Helping Small Businesses At An Affordable Rate) (Work With A Local Colorado Company To Get The Help You Need)

Industry/Entity Type

Private equity / Financial Services / Manage Services / Marketing / Business Solutions

Requirements
Must have
• Needs to have address 2450 Marlow St. 12th Floor, Denver CO 80207 Phone number 303-542-7318 email: info@birchlaneassociates.com needs to have all the services on the list provided. Needs to have (Get A Solution For Your Companies Business Solutions) website: www.birchlaneassociates.com

```html
<!DOCTYPE html>
<html lang="en">
<head>
<meta charset="utf-8">
<title>Birch Lane Associates – Business Solutions Flyer</title>
<link href="https://fonts.googleapis.com/css2?family=Roboto:wght@400;500;700&family=Roboto+Condensed:wght@700&display=swap" rel="stylesheet">
<style>
  :root {
    --maroon: #7b262c;
    --ink: #111111;
    --white: #ffffff;
  }
  * { margin: 0; padding: 0; box-sizing: border-box; }
  html, body { width: 848px; height: 1200px; overflow: hidden; background: var(--white); }
  .flyer {
    position: relative; width: 848px; height: 1200px; overflow: hidden;
    font-family: "Roboto", Arial, sans-serif; color: var(--ink); background: var(--white);
  }
  .brand { position: absolute; left: 54px; top: 42px; display: flex; align-items: center; gap: 14px; }
  .brand-square { width: 52px; height: 52px; background: var(--maroon); }
  .brand-name { font-weight: 700; font-size: 30px; color: var(--ink); letter-spacing: 0.5px; line-height: 1; }

  .hero-photo { position: absolute; left: 0; top: 0; width: 848px; height: 341px; }

  .headline {
    position: absolute; left: 0; width: 503px; top: 126px; text-align: center;
    font-family: "Roboto Condensed", "Arial Narrow", sans-serif; font-weight: 700; font-size: 43px; line-height: 46px;
  }
  .headline .accent { color: var(--maroon); display: block; }
  .headline .dark { color: var(--ink); display: block; }
  .headline-rule { position: absolute; left: 69px; top: 223px; width: 353px; height: 2px; background: var(--maroon); }
  .subhead {
    position: absolute; left: 0; width: 494px; top: 233px; text-align: center;
    font-size: 25.8px; line-height: 31px; font-weight: 400;
  }

  .section-band { position: absolute; left: 0; width: 848px; height: 67px; background: var(--maroon); }
  .section-badge {
    position: absolute; left: 53px; width: 116px; height: 116px; border-radius: 50%;
    background: var(--maroon); display: flex; align-items: center; justify-content: center;
  }
  .section-title {
    position: absolute; font-weight: 700; font-size: 25px;
    color: var(--white); line-height: 67px;
  }
  .financial .section-band { top: 341px; }
  .financial .section-badge { top: 313px; }
  .financial .section-title { left: 183px; top: 341px; }
  .marketing .section-band { top: 693px; }
  .marketing .section-badge { top: 666px; }
  .marketing .section-title { left: 185px; top: 693px; }

  .service-list { position: absolute; list-style: none; font-size: 22.5px; line-height: 27.4px; }
  .service-list li::before { content: "•"; display: inline-block; width: 13px; font-size: 16px; vertical-align: 3px; }
  .financial .col-a { left: 63px; top: 447px; }
  .financial .col-b { left: 403px; top: 447px; }
  .marketing .col-a { left: 63px; top: 799px; }
  .marketing .col-b { left: 403px; top: 799px; }

  .roofline { position: absolute; left: 0; top: 0; width: 848px; height: 1200px; }

  .contact { position: absolute; left: 0; top: 1040px; width: 848px; height: 160px; color: var(--white); }
  .contact-tagline { position: absolute; left: 30px; top: 18px; font-family: "Roboto Condensed", "Arial Narrow", sans-serif; font-weight: 700; font-size: 25.5px; }
  .contact-line { position: absolute; left: 37px; display: flex; align-items: center; gap: 14px; }
  .contact-line svg { width: 20px; height: 20px; flex: none; }
  .contact-address { top: 62px; font-size: 17.5px; }
  .contact-phone { top: 88px; font-size: 21px; font-weight: 700; }
  .contact-email { top: 120px; font-size: 17.5px; }
  .contact-web { position: absolute; right: 51px; top: 120px; font-size: 17.5px; }
  .contact-mark { position: absolute; left: 659px; top: 30px; width: 72px; height: 70px; border: 11px solid var(--white); }
</style>
</head>
<body>
<main class="flyer">

  <svg class="hero-photo" viewBox="0 0 848 341" role="img" aria-label="Photo of a hand touching a rising financial chart on a digital grid">
    <defs>
      <linearGradient id="photoTone" x1="0" y1="0" x2="1" y2="1">
        <stop offset="0" stop-color="#2c2f34"/>
        <stop offset="0.55" stop-color="#5c6168"/>
        <stop offset="1" stop-color="#8fa7bd"/>
      </linearGradient>
    </defs>
    <path d="M565 0 C560 60 500 100 495 165 C492 230 530 260 510 341 L848 341 L848 0 Z" fill="#e2e2e2"/>
    <path d="M577 0 C572 62 512 102 507 165 C504 230 542 262 520 341 L848 341 L848 0 Z" fill="url(#photoTone)"/>
  </svg>

  <header class="brand">
    <span class="brand-square"></span>
    <span class="brand-name">Birch Lane Associates</span>
  </header>

  <h1 class="headline">
    <span class="accent">Helping Small Businesses</span>
    <span class="dark">At An Affordable Rate</span>
  </h1>
  <div class="headline-rule"></div>
  <p class="subhead">Work With A Local Colorado Company<br>To Get The Help You Need</p>

  <section class="financial">
    <div class="section-band"></div>
    <div class="section-badge">
      <svg width="70" height="66" viewBox="0 0 70 66" fill="none" stroke="#fff" stroke-width="2.2">
        <rect x="3" y="3" width="64" height="56"/>
        <rect x="8" y="8" width="54" height="24"/>
        <polyline points="14,27 23,17 31,22 42,14 52,16"/>
        <circle cx="23" cy="17" r="2"/><circle cx="42" cy="14" r="2"/>
        <line x1="10" y1="38" x2="60" y2="38"/><line x1="10" y1="44" x2="60" y2="44"/><line x1="10" y1="50" x2="60" y2="50"/>
        <path d="M29 59 v4 h12 v-4"/>
      </svg>
    </div>
    <h2 class="section-title">Financial Services</h2>
    <ul class="service-list col-a">
      <li>Cash flow management</li>
      <li>Tax planning</li>
      <li>Alternative funding</li>
      <li>Asset leasing</li>
      <li>Bookkeeping service</li>
      <li>Expense reduction</li>
      <li>Real estate appraising</li>
    </ul>
    <ul class="service-list col-b">
      <li>Budgeting &amp; forecasting</li>
      <li>Profit and Loss (P&amp;L) Statement</li>
      <li>Business financing</li>
      <li>Financial statement analysis</li>
      <li>Business valuation</li>
      <li>Legal services</li>
    </ul>
  </section>

  <section class="marketing">
    <div class="section-band"></div>
    <div class="section-badge">
      <svg width="70" height="70" viewBox="0 0 70 70" fill="none" stroke="#fff" stroke-width="2.2">
        <circle cx="18" cy="26" r="13"/>
        <rect x="14" y="41" width="8" height="22" rx="4"/>
        <line x1="18" y1="39" x2="18" y2="41"/>
        <rect x="36" y="26" width="4" height="16"/><rect x="44" y="20" width="4" height="22"/>
        <rect x="52" y="14" width="4" height="28"/><rect x="60" y="8" width="4" height="34"/>
        <polyline points="30,22 56,4"/><polyline points="49,3 56,4 55,11"/>
        <line x1="34" y1="50" x2="64" y2="50"/><line x1="34" y1="56" x2="64" y2="56"/><line x1="34" y1="62" x2="64" y2="62"/>
      </svg>
    </div>
    <h2 class="section-title">Marketing &amp; Advertising Services</h2>
    <ul class="service-list col-a">
      <li>Search engine advertising</li>
      <li>Direct mail marketing</li>
      <li>Email marketing</li>
      <li>Social media targeting</li>
      <li>SEO</li>
    </ul>
    <ul class="service-list col-b">
      <li>Logo design</li>
      <li>Website design</li>
      <li>Flyer design</li>
      <li>Business card design</li>
      <li>Brochure design</li>
    </ul>
  </section>

  <svg class="roofline" viewBox="0 0 848 1200" aria-hidden="true">
    <polygon fill="var(--maroon)" points="0,991 580,991 695,876 810,991 848,991 848,1019 797,1019 695,917 593,1019 0,1019"/>
    <polygon fill="var(--maroon)" points="0,1040 605,1040 695,950 785,1040 848,1040 848,1200 0,1200"/>
  </svg>

  <footer class="contact">
    <p class="contact-tagline">Get A Solution For Your Companies Business Solutions</p>
    <p class="contact-line contact-address">
      <svg viewBox="0 0 20 20"><path fill="#fff" d="M10 1a6.5 6.5 0 0 0-6.5 6.5C3.5 12 10 19 10 19s6.5-7 6.5-11.5A6.5 6.5 0 0 0 10 1zm0 9a2.5 2.5 0 1 1 0-5 2.5 2.5 0 0 1 0 5z"/></svg>
      2450 Marlow St. 12th Floor, Denver CO 80207
    </p>
    <p class="contact-line contact-phone">
      <svg viewBox="0 0 20 20"><path fill="#fff" d="M4.5 1.5l3 3.5-2 2.2c1.2 2.6 3.2 4.6 5.8 5.8l2.2-2 3.5 3-1.6 3c-7.5-.5-12.9-5.9-13.4-13.4z"/></svg>
      303-542-7318
    </p>
    <p class="contact-line contact-email">
      <svg viewBox="0 0 20 20"><path fill="#fff" d="M1 4h18v1.5l-9 5.5-9-5.5zM1 7.5l9 5.5 9-5.5V16H1z"/></svg>
      info@birchlaneassociates.com
    </p>
    <div class="contact-mark"></div>
    <p class="contact-web">www.birchlaneassociates.com</p>
  </footer>

</main>
</body>
</html>
```